Graphic Design for tolvi clothing.ca

a hip vegan clothing line, also gay friendly that is launching in august 2012. trendy, funky, studs, pleather, sequins, bright colours... hippie/80's style.

```html
<!DOCTYPE html>
<html lang="en">
<head>
<meta charset="utf-8">
<title>Tolvi clothing – Coming soon</title>
<link rel="stylesheet" href="https://fonts.googleapis.com/css2?family=Almendra:wght@400;700&family=Source+Sans+3:wght@400;600&display=swap">
<style>
  :root {
    --wood-dark: #1a0703;
    --wood-mid: #4a1508;
    --wood-warm: #7a2a0e;
    --title-top: #ffb347;
    --title-bottom: #e2501a;
    --text-light: #ffffff;
    --launch-gold: #b38a3c;
    --sign-face: #3a0e06;
    --sign-edge: #1c0502;
    --sign-text: #2a0804;
  }
  * { margin: 0; padding: 0; box-sizing: border-box; }
  html, body { width: 1200px; height: 772px; overflow: hidden; background: var(--wood-dark); }
  .teaser {
    position: relative;
    width: 1200px;
    height: 772px;
    overflow: hidden;
    font-family: "Source Sans 3", "Myriad Pro", sans-serif;
    color: var(--text-light);
    background:
      radial-gradient(ellipse 55% 50% at 50% 50%, rgba(140,50,15,0.55), transparent 75%),
      repeating-linear-gradient(93deg, rgba(0,0,0,0.12) 0 3px, transparent 3px 19px),
      radial-gradient(ellipse 80% 75% at 50% 48%, var(--wood-warm), var(--wood-mid) 45%, var(--wood-dark) 90%);
  }
  .teaser__coming {
    position: absolute; left: 155px; top: 22px;
    font-size: 48px; font-weight: 400; letter-spacing: 1px;
    white-space: nowrap;
  }
  .teaser__tagline {
    position: absolute; left: 553px; top: 86px;
    font-size: 33px; font-weight: 400;
    white-space: nowrap;
  }
  .teaser__brand {
    position: absolute; left: 0; right: 0; top: 118px;
    text-align: center;
    font-family: "Almendra", serif;
    font-size: 118px; font-weight: 400; letter-spacing: 6px;
    line-height: 1.1;
    white-space: nowrap;
    background: linear-gradient(180deg, var(--title-top), var(--title-bottom));
    -webkit-background-clip: text; background-clip: text;
    color: transparent;
  }
  .teaser__mark {
    position: absolute; left: 500px; top: 320px;
    width: 200px; height: 200px; border-radius: 50%;
    background: radial-gradient(circle, #000 55%, #3a1200 66%, transparent 72%);
    box-shadow: 0 0 70px 18px rgba(255,160,60,0.55);
  }
  .sign {
    position: absolute;
    width: 250px; height: 60px;
    background: linear-gradient(180deg, #4a140a, var(--sign-face) 60%, #2a0904);
    border: 2px solid var(--sign-edge);
    box-shadow: 0 6px 10px rgba(0,0,0,0.55), inset 0 1px 0 rgba(255,120,60,0.15);
    font-size: 34px; line-height: 56px; text-align: center;
    color: var(--sign-text);
    text-shadow: 0 1px 0 rgba(255,120,60,0.2);
  }
  .sign--vegan { left: 150px; top: 325px; transform: rotate(8deg); }
  .sign--hippie { left: 140px; top: 405px; transform: rotate(-5deg); }
  .sign--vests { left: 150px; top: 500px; transform: rotate(8deg); }
  .sign--denim { left: 823px; top: 305px; transform: rotate(-5deg); }
  .sign--sequins { left: 825px; top: 415px; transform: rotate(-8deg); }
  .sign--studs { left: 820px; top: 505px; transform: rotate(2deg); }
  .teaser__launch {
    position: absolute; left: 51px; top: 690px;
    font-size: 41px; color: var(--launch-gold);
    white-space: nowrap;
  }
  .follow {
    position: absolute; right: 32px; top: 700px;
    display: flex; align-items: center; gap: 14px;
    white-space: nowrap;
  }
  .follow__label {
    font-size: 22px; font-weight: 600;
  }
  .follow__network {
    font-size: 17px; font-weight: 600; color: var(--text-light);
  }
</style>
</head>
<body>
  <main class="teaser">
    <p class="teaser__coming">Coming soon. .</p>
    <p class="teaser__tagline">Let’s find who is behind,</p>
    <h1 class="teaser__brand">Tolvi clothing</h1>
    <div class="teaser__mark" role="img" aria-label="Glowing brand mark area"></div>

    <div class="sign sign--vegan">Vegan</div>
    <div class="sign sign--hippie">Hippie</div>
    <div class="sign sign--vests">Vests</div>
    <div class="sign sign--denim">Denim</div>
    <div class="sign sign--sequins">Sequins</div>
    <div class="sign sign--studs">Studs</div>

    <p class="teaser__launch">Launching August 2012</p>
    <div class="follow">
      <span class="follow__label">Follow us on</span>
      <span class="follow__network">Chirper</span>
      <span class="follow__network">Facepage</span>
      <span class="follow__network">Pinboard</span>
    </div>
  </main>
</body>
</html>
```